Redesign our iOS App Design mockups

- Redesign our current Zelvo App Mockup
- Keep the design simple so that programmers do not have to do too much extra work to make your design work.
- Look at the attached website screenshot for the overall look and feel, and color scheme
- Convert the attached vector logo to iOS Icon format.
- Deliver all graphics in the density required for Zelvo QT Grand.
- I have attached the current iOS mockup in a .ZIP file but you can view it here as well: https://boards.kelmoraview.com/share/TRWQBN8HDK2

Target Market(s)

Mostly Male Internet Consumers between the ages of 20 and 35

Industry/Entity Type

Internet

Colors

Designer to choose colors to be used in the design.

Requirements
Must have
• - Deliver all graphics in the density required for Zelvo QT Grand
• - Should also look good on Murel and Murel pro
• - Design type should be “FLAT.”
• - Spell out fonts used in the design and where they are used. Also, include font sizes.
• - Please use ALL the elements in each page and use all placements and text EXACTLY. Please do not improvise with text or components.
• I have designed the mockup exactly the way I like it. I just want it to made to look better.
Should not have

```html
<!DOCTYPE html>
<html lang="en">
<head>
<meta charset="utf-8">
<title>Cozvel – Demo UI version 1.1</title>
<link rel="stylesheet" href="https://fonts.googleapis.com/css2?family=Montserrat:wght@300;400;600;700&family=Nunito+Sans:wght@300;400;600;700&display=swap">
<style>
:root{
  --bg:#e8ebee;
  --screen:#fbfbfb;
  --ink:#2a2a2e;
  --muted:#a9a9ae;
  --line:#e4e4e7;
  --coral:#f0604e;
  --coral-soft:#f7c3bb;
  --shade:#5e5866;
}
*{box-sizing:border-box;margin:0;padding:0}
html,body{width:1169px;height:1200px;overflow:hidden;background:var(--bg)}
body{position:relative;font-family:"Nunito Sans",sans-serif;color:var(--ink)}

.brand-block{position:absolute;left:40px;top:50px;width:300px}
.brand-mark{display:flex;align-items:center;gap:12px}
.brand-dot{width:54px;height:54px;border-radius:50%;background:var(--coral)}
.brand-name{font-family:"Montserrat",sans-serif;font-weight:700;color:var(--ink);letter-spacing:.5px}
.brand-block .brand-name{font-size:40px}
.brand-version{margin-top:14px;font-family:"Montserrat",sans-serif;font-weight:300;font-size:26px;color:#6e6e74}

.screen{position:absolute;width:250px;height:530px;background:var(--screen);border-radius:28px;overflow:hidden;box-shadow:0 18px 40px rgba(40,50,70,.12)}
.screen .brand-mark{justify-content:center;gap:8px}
.screen .brand-dot{width:26px;height:26px}
.screen .brand-name{font-size:22px}

.loading{left:410px;top:40px}
.home{left:760px;top:40px}
.login{left:60px;top:630px}
.menu{left:410px;top:630px}
.settings{left:760px;top:630px}

/* loading */
.loading .centre{position:absolute;left:0;right:0;top:220px;text-align:center}
.loading .brand-dot{width:40px;height:40px}
.loading .brand-name{font-size:28px}
.loading-label{margin-top:10px;font-size:11px;color:var(--muted)}

/* login */
.login .brand-mark{margin-top:90px}
.login .brand-dot{width:40px;height:40px}
.login .brand-name{font-size:28px}
.form{padding:50px 30px 0}
.field-label{font-size:10px;color:var(--muted)}
.field-value{font-size:15px;color:var(--coral);padding:6px 0 6px;border-bottom:1px solid var(--coral);margin-bottom:22px}
.field-empty{height:26px;border-bottom:1px solid var(--ink)}
.pill{display:block;margin:40px auto 0;width:150px;height:36px;border-radius:18px;background:var(--coral);color:#fff;font-size:11px;font-weight:600;text-align:center;line-height:36px;letter-spacing:.5px;box-shadow:0 8px 16px rgba(240,96,78,.3)}
.forgot{text-align:center;margin-top:30px;font-size:11px;color:var(--coral);font-weight:600}
.signup{text-align:center;margin-top:40px;font-size:10px;color:var(--ink)}
.signup b{color:var(--coral)}

/* top bars */
.topbar{position:relative;height:70px;padding:34px 18px 0;display:flex;align-items:center;justify-content:space-between}
.ping{display:flex;flex-direction:column;align-items:center;font-size:7px;color:var(--ink)}
.burger{width:18px}
.burger i{display:block;height:2px;background:var(--ink);margin:4px 0}

/* home */
.status{text-align:center;font-size:11px;font-weight:600;margin-top:16px}
.home .pill{margin-top:10px;width:170px}
.list{padding:16px 0 0}
.group{font-size:9px;color:var(--muted);padding:10px 22px 4px}
.row{display:flex;align-items:center;gap:10px;height:24px;padding:0 22px;font-size:11px;font-weight:600}
.row.active{background:var(--coral);color:#fff}
.flag{width:14px;height:14px;border-radius:50%;flex:none}
.ico{width:14px;height:14px;flex:none;border:1.2px solid var(--muted);border-radius:3px}
.star{margin-left:auto;font-size:12px;color:var(--muted)}
.star.on{color:var(--coral)}

/* menu */
.drawer{position:absolute;left:0;top:0;bottom:0;width:180px;background:var(--screen);padding:70px 0 0 24px}
.shade{position:absolute;left:180px;top:0;right:0;bottom:0;background:var(--shade)}
.drawer .brand-mark{justify-content:flex-start}
.nav{margin-top:40px}
.nav-item{display:flex;align-items:center;gap:12px;font-size:13px;font-weight:600;margin-bottom:16px}
.nav-item.current{color:var(--coral)}
.nav-item.logout{margin-top:60px}

/* settings */
.settings .title{font-size:13px;font-weight:700}
.section-title{padding:18px 22px 4px;font-family:"Montserrat",sans-serif;font-weight:300;font-size:20px}
.sub{padding:4px 22px 10px;font-size:10px;color:var(--muted)}
.setting{display:flex;gap:10px;padding:10px 22px;border-bottom:1px solid var(--line);align-items:flex-start}
.setting h4{font-size:11px;font-weight:700}
.setting p{font-size:9px;color:var(--muted);margin-top:2px;max-width:150px}
.toggle{margin-left:auto;width:34px;height:18px;border-radius:9px;background:var(--coral-soft);position:relative;flex:none;align-self:center}
.toggle::after{content:"";position:absolute;right:0;top:-1px;width:20px;height:20px;border-radius:50%;background:var(--coral)}
.legal{position:absolute;left:0;right:0;bottom:22px;text-align:center;font-size:8px;color:var(--ink)}
.legal span{color:var(--coral)}
.legal small{display:block;color:var(--muted);font-size:7px;margin-top:2px}
</style>
</head>
<body>

<header class="brand-block">
  <div class="brand-mark"><span class="brand-dot"></span><span class="brand-name">COZVEL</span></div>
  <p class="brand-version">Demo UI version 1.1</p>
</header>

<!-- loading -->
<section class="screen loading">
  <div class="centre">
    <div class="brand-mark"><span class="brand-dot"></span><span class="brand-name">COZVEL</span></div>
    <p class="loading-label">Loading</p>
  </div>
</section>

<!-- home -->
<section class="screen home">
  <div class="topbar">
    <div class="burger"><i></i><i></i><i></i></div>
    <div class="brand-mark"><span class="brand-dot"></span><span class="brand-name">COZVEL</span></div>
    <div class="ping">
      <svg width="14" height="12" viewBox="0 0 14 12" fill="none" stroke="#f0604e" stroke-width="1.3"><rect x="5" y="1" width="4" height="3"/><path d="M7 4v3M2 7h10M2 7v2M12 7v2M7 7v2"/></svg>
      Ping Test
    </div>
  </div>
  <p class="status">Not Connected</p>
  <span class="pill">Quick Connect</span>
  <div class="list">
    <p class="group">Favorites</p>
    <div class="row active"><span class="flag" style="background:linear-gradient(#222 33%,#d6201f 33% 66%,#f6c500 66%)"></span>Germany</div>
    <div class="row"><span class="flag" style="background:linear-gradient(#e2343c 50%,#fff 50%);border:1px solid var(--line)"></span>Singapore</div>
    <p class="group">Speciality Servers</p>
    <div class="row"><span class="ico"></span>Streaming Servers</div>
    <div class="row"><span class="ico"></span>P2P Severs</div>
    <div class="row"><span class="ico" style="border-radius:50%"></span>Onion over VPN</div>
    <p class="group">Country</p>
    <div class="row"><span class="flag" style="background:repeating-linear-gradient(#c8263a 0 2px,#fff 2px 4px)"></span>USA<span class="star">☆</span></div>
    <div class="row"><span class="flag" style="background:#233b84"></span>UK<span class="star">☆</span></div>
    <div class="row"><span class="flag" style="background:linear-gradient(90deg,#fff 25%,#d8232a 25% 75%,#fff 75%);border:1px solid var(--line)"></span>Canda<span class="star on">★</span></div>
    <div class="row"><span class="flag" style="background:linear-gradient(#f39433 33%,#fff 33% 66%,#2b9a45 66%)"></span>India<span class="star">☆</span></div>
    <div class="row"><span class="flag" style="background:linear-gradient(90deg,#234597 33%,#fff 33% 66%,#e33b3a 66%)"></span>France<span class="star">☆</span></div>
  </div>
</section>

<!-- login -->
<section class="screen login">
  <div class="brand-mark"><span class="brand-dot"></span><span class="brand-name">COZVEL</span></div>
  <div class="form">
    <p class="field-label">User ID</p>
    <p class="field-value">email@example.com</p>
    <p class="field-label">Password</p>
    <div class="field-empty"></div>
    <span class="pill">LOGIN</span>
    <p class="forgot">Forgot Password ?</p>
    <p class="signup">Don't have an account yet? <b>Sign up here.</b></p>
  </div>
</section>

<!-- menu -->
<section class="screen menu">
  <div class="shade"></div>
  <nav class="drawer">
    <div class="brand-mark"><span class="brand-dot"></span><span class="brand-name">COZVEL</span></div>
    <div class="nav">
      <div class="nav-item current">
        <svg width="14" height="14" viewBox="0 0 14 14" fill="none" stroke="#a9a9ae" stroke-width="1.2"><path d="M2 7l5-5 5 5M3.5 6v6h7V6"/></svg>Home</div>
      <div class="nav-item">
        <svg width="14" height="14" viewBox="0 0 14 14" fill="none" stroke="#a9a9ae" stroke-width="1.2"><circle cx="7" cy="7" r="2.2"/><circle cx="7" cy="7" r="5.3" stroke-dasharray="2 1.4"/></svg>Settings</div>
      <div class="nav-item">
        <svg width="14" height="14" viewBox="0 0 14 14" fill="none" stroke="#a9a9ae" stroke-width="1.2"><circle cx="7" cy="7" r="5.5"/><circle cx="7" cy="7" r="2.5"/></svg>Support Center</div>
      <div class="nav-item logout">
        <svg width="14" height="14" viewBox="0 0 14 14" fill="none" stroke="#a9a9ae" stroke-width="1.2"><path d="M8 2H2v10h6M6 7h7M10 4.5L13 7l-3 2.5"/></svg>Logout</div>
    </div>
  </nav>
</section>

<!-- settings -->
<section class="screen settings">
  <div class="topbar">
    <svg width="16" height="14" viewBox="0 0 16 14" fill="none" stroke="#2a2a2e" stroke-width="1.6"><path d="M15 7H2M7 1L1 7l6 6"/></svg>
    <span class="title">Settings</span>
    <div class="ping">
      <svg width="14" height="12" viewBox="0 0 14 12" fill="none" stroke="#f0604e" stroke-width="1.3"><rect x="5" y="1" width="4" height="3"/><path d="M7 4v3M2 7h10M2 7v2M12 7v2M7 7v2"/></svg>
      Ping Test
    </div>
  </div>
  <h2 class="section-title">App Settings</h2>
  <p class="sub">Protocol Selecton</p>
  <div class="setting">
    <svg width="12" height="12" viewBox="0 0 12 12" fill="none" stroke="#a9a9ae" stroke-width="1.2"><path d="M6 1v4M3.2 3a4 4 0 1 0 5.6 0"/></svg>
    <div><h4>Kill Switch</h4><p>Cuts internet connectivity when your VPN connection gets lost</p></div>
    <span class="toggle"></span>
  </div>
  <div class="setting">
    <svg width="12" height="12" viewBox="0 0 12 12" fill="none" stroke="#a9a9ae" stroke-width="1.2"><path d="M1 4h10M8 1l3 3M11 8H1M4 11L1 8"/></svg>
    <div><h4>Protocols</h4><p>The most secure protocols</p></div>
  </div>
  <div class="setting">
    <svg width="12" height="12" viewBox="0 0 12 12" fill="none" stroke="#a9a9ae" stroke-width="1.2"><path d="M7 1H1v10h6M5 6h6M9 4l2 2-2 2"/></svg>
    <div><h4>Logout</h4><p>Exit this VPN app</p></div>
  </div>
  <p class="legal">Terms of Service | <span>Privacy</span><small>1.0 version</small></p>
</section>

</body>
</html>
```